Business card design based on existing website

Please make a business card that is consistent with the look and feel of my new website: http://tellbury.com.sg. By going to the site, I think you'll have all you need in terms of the work I do and the colors I use.

I would like to ask the winner of this project to then do a separate project to design my stationery.

Target Market(s)

Heads of human resources, people wanting psychotherapy, and executives wanting coaching. (It's quite a mix!)

Industry/Entity Type

Psychology

Contact Information for Business Card

Email: ray5678@tellbury.com.sg
Website: http://tellbury.com.sg
Tel: +65 94706218

(I will not have a physical address on the card)

Font styles to use
Serif

Colors

Designer to choose colors to be used in the design.

Requirements
Must have
• On the Front
• ==========
• Have "Dr. Raymond Tellbury" using the font of the website.
• Also "Executive Coach, Psychotherapist, Leadership Professor"
• The back should mention
• ==================
• My degrees
• -------------
• "PhD Kelworth; Post Doc Drayfield". E.g., "Raymond Tellbury (PhD Kelworth; Post Doc Drayfield)" where the text between brackets was in smaller font.
• My work
• ----------
• "Executive coach, psychotherapist, and leadership professor"
• My job titles
• ---------------
• "Principal (Tellbury Consulting)
• Adjunct Professor (Lornvale Commerce University)
• Adjunct Associate Professor (Pemberly Institute of Letters)
• Coach & Supervisor (OKTRAV) '
• Options:
• 1) you can abbreviate Adjunct Professor to "Adj Prof" or "Adj Professor"; and "Adjunct Associate Professor" to "Adj Assoc Prof"
• 2) you abbreviate "Pemberly Institute of Letters" and "Lornvale Commerce University" to "PIL" and "LCU"
• 3) You can also combine the titles for PIL and LCU, e.g., "Adjunct faculty (PIL & LCU)
Nice to have
• Because I work with many Chinese people, it is sometimes helpful to have my family name, "Tellbury", in caps. In the past I have not used caps because it takes away from the aesthetic of the card. Only use caps if it looks good.
• The uploaded image of a "RT" is something that may be helpful. I am undecided.
• THANK YOU for helping me!
Should not have
• No photos. In my industry people consider it overselling.

```html
<!DOCTYPE html>
<html lang="en">
<head>
<meta charset="utf-8">
<title>Dr. Raymond Tellbury – Business Card</title>
<link rel="stylesheet" href="https://fonts.googleapis.com/css2?family=Jost:wght@600&family=Lato:wght@400&display=swap">
<style>
  :root {
    --backdrop: #e9e6e1;
    --card-black: #111211;
    --accent-yellow: #e6e51f;
    --text-light: #ecece8;
    --text-soft: #c9c9c4;
    --rule-grey: #5a5a58;
    --foliage-deep: #0c1a0f;
    --foliage-mid: #1f3a26;
    --foliage-light: #2f5236;
  }
  * { margin: 0; padding: 0; box-sizing: border-box; }
  html, body {
    width: 1200px; height: 900px; overflow: hidden;
    background: var(--backdrop);
  }
  .canvas { position: relative; width: 1200px; height: 900px; }

  .card {
    position: absolute;
    width: 525px; height: 300px;
    border-radius: 3px;
    overflow: hidden;
    box-shadow: 0 10px 28px rgba(0,0,0,0.22);
  }

  /* Back of card */
  .card-back {
    left: 120px; top: 120px;
    background: var(--card-black);
    display: flex; flex-direction: column; align-items: center; justify-content: center;
    text-align: center;
    font-family: "Lato", sans-serif;
    color: var(--text-light);
  }
  .tagline {
    font-family: "Jost", sans-serif;
    font-weight: 600;
    font-size: 20px;
    line-height: 1.05;
    letter-spacing: 0.06em;
    color: var(--accent-yellow);
    text-transform: uppercase;
  }
  .divider {
    width: 270px; height: 1px;
    background: var(--rule-grey);
    margin: 10px 0 9px;
  }
  .credentials { font-size: 14px; line-height: 1.4; letter-spacing: 0.02em; }
  .degrees { font-size: 11.5px; color: var(--text-soft); }
  .work { font-size: 13px; line-height: 1.4; letter-spacing: 0.02em; }
  .titles { list-style: none; font-size: 13px; line-height: 1.4; letter-spacing: 0.02em; }

  /* Front of card */
  .card-front {
    left: 555px; top: 470px;
    background:
      radial-gradient(ellipse 70% 80% at 70% 30%, var(--foliage-light) 0%, var(--foliage-mid) 50%, rgba(31,58,38,0) 100%),
      linear-gradient(90deg, var(--foliage-deep) 0%, var(--foliage-mid) 60%, var(--foliage-deep) 100%);
  }
  .front-text {
    position: absolute; left: 34px; top: 140px; right: 34px;
    font-family: "Lato", sans-serif;
    color: var(--text-light);
  }
  .name {
    font-family: "Jost", sans-serif;
    font-weight: 600;
    font-size: 22px;
    letter-spacing: 0.04em;
    color: var(--accent-yellow);
    text-transform: uppercase;
  }
  .role-line {
    font-size: 13px;
    letter-spacing: 0.02em;
    color: var(--text-soft);
    margin: 4px 0 22px;
  }
  .contact-list { list-style: none; font-size: 15px; line-height: 1.5; }
  .contact-item { display: flex; align-items: center; gap: 8px; }
  .contact-icon { width: 14px; height: 14px; flex: none; }
</style>
</head>
<body>
<main class="canvas">

  <section class="card card-back" aria-label="Business card back">
    <h2 class="tagline">Advancing Human<br>Development</h2>
    <div class="divider"></div>
    <p class="credentials">Raymond Tellbury <span class="degrees">(PhD Kelworth; Post Doc Drayfield)</span></p>
    <p class="work">Executive coach, psychotherapist, and leadership professor</p>
    <div class="divider"></div>
    <ul class="titles">
      <li>Principal (Tellbury Consulting)</li>
      <li>Adj Prof (LCU)</li>
      <li>Adj Assoc Prof (PIL)</li>
      <li>Coach &amp; Supervisor (OKTRAV)</li>
    </ul>
  </section>

  <section class="card card-front" aria-label="Business card front">
    <div class="front-text">
      <h1 class="name">Dr. Raymond Tellbury</h1>
      <p class="role-line">Executive Coach, Psychotherapist, Leadership Professor</p>
      <ul class="contact-list">
        <li class="contact-item">
          <svg class="contact-icon" viewBox="0 0 14 14" aria-hidden="true">
            <rect x="1" y="3" width="12" height="9" rx="1.5" fill="var(--accent-yellow)"/>
            <path d="M2 4.5 Q7 0.5 12 4.5" stroke="var(--accent-yellow)" stroke-width="2" fill="none"/>
            <circle cx="7" cy="8" r="2" fill="var(--foliage-deep)"/>
          </svg>
          <span>+65 94706218</span>
        </li>
        <li class="contact-item">
          <svg class="contact-icon" viewBox="0 0 14 14" aria-hidden="true">
            <rect x="1" y="3" width="12" height="8.5" fill="var(--accent-yellow)"/>
            <path d="M1.5 3.5 L7 8 L12.5 3.5" stroke="var(--foliage-deep)" stroke-width="1.1" fill="none"/>
          </svg>
          <span>ray5678@tellbury.com.sg</span>
        </li>
        <li class="contact-item">
          <svg class="contact-icon" viewBox="0 0 14 14" aria-hidden="true">
            <circle cx="7" cy="7" r="6" fill="var(--accent-yellow)"/>
            <path d="M1 7 H13 M7 1 Q3.5 7 7 13 M7 1 Q10.5 7 7 13" stroke="var(--foliage-deep)" stroke-width="1" fill="none"/>
          </svg>
          <span>www.tellbury.com.sg</span>
        </li>
      </ul>
    </div>
  </section>

</main>
</body>
</html>
```